New Web Design Project

See attachments on the content and concept. Very important that the flow of the tiers stand out

Target Market(s)

Food and Beverage Manufacturing

Industry/Entity Type

Food and Beverage

Coding

Coded - Design and coding required

Number of Pages Required

3 page

Colors
0054AA
0677BA
7BADD7
CADEEF
E8F1F8

```html
<!DOCTYPE html>
<html lang="en">
<head>
<meta charset="utf-8">
<title>Crestline Consulting Group — SQF Consulting</title>
<link rel="stylesheet" href="https://fonts.googleapis.com/css2?family=Poppins:wght@400;500;600;700&display=swap">
<style>
:root{
  --navy:#0054AA;
  --blue:#0677BA;
  --sky:#7BADD7;
  --mist:#CADEEF;
  --ice:#E8F1F8;
  --ink:#111827;
  --text:#374151;
  --muted:#4b5563;
  --line:#e5e7eb;
  --white:#ffffff;
}
*{box-sizing:border-box;margin:0;padding:0}
html,body{width:1200px;height:3830px;overflow:hidden;background:var(--white)}
body{font-family:'Poppins',sans-serif;color:var(--ink);position:relative}
.abs{position:absolute}
.btn{position:absolute;display:flex;align-items:center;justify-content:center;border-radius:10px;font-size:15px;font-weight:500;text-decoration:none}
.btn-solid{background:var(--navy);color:var(--white)}
.btn-ghost{background:var(--white);color:var(--navy);border:2px solid var(--navy)}
.eyebrow{font-size:12px;font-weight:600;color:var(--blue);letter-spacing:.3px;text-transform:uppercase}
.center{text-align:center;left:0;width:1200px}

/* nav */
.brand{left:60px;top:30px;display:flex;align-items:center;gap:10px;font-size:17px;font-weight:600;color:var(--ink)}
.brand-mark{width:22px;height:22px;border:2px solid var(--ink);border-radius:4px}
.nav-links{left:302px;top:34px;display:flex;gap:50px;font-size:15px;color:var(--text)}
.nav-links .active{color:var(--navy);font-weight:600;text-decoration:underline;text-underline-offset:5px}
.theme-toggle{left:985px;top:34px}

/* hero */
.hero-title{left:60px;top:146px;width:580px;font-size:40px;line-height:60px;font-weight:600}
.hero-copy{left:60px;top:336px;width:570px;font-size:20px;line-height:38px;color:var(--text)}
.hero-photo{left:668px;top:110px;width:472px;height:452px;border-radius:13px;background:linear-gradient(160deg,#dfe5ea 0%,#b8c2cb 45%,#8e99a3 100%)}

.stats{left:60px;top:603px;width:1080px;height:109px;border:1.5px solid var(--line);border-radius:13px;box-shadow:0 3px 10px rgba(0,0,0,.05);display:grid;grid-template-columns:230px 240px 340px 270px}
.stat{text-align:center;padding-top:14px}
.stat b{display:block;font-size:36px;font-weight:600;color:var(--navy);line-height:48px}
.stat span{font-size:15px;color:var(--text)}

.section-title{font-size:35px;line-height:47px;font-weight:600}
.section-sub{font-size:15px;line-height:25px;color:var(--text)}

/* services */
.cards{left:60px;top:963px;width:1080px;display:grid;grid-template-columns:repeat(3,345px);gap:16px 22px}
.card{height:299px;border:1.5px solid var(--line);border-radius:16px;padding:22px 22px;box-shadow:0 2px 8px rgba(0,0,0,.04)}
.card-icon{width:50px;height:50px;border-radius:8px;background:var(--ice);display:flex;align-items:center;justify-content:center}
.card h3{font-size:18px;font-weight:600;margin:45px 0 14px}
.card p{font-size:14px;line-height:22.5px;color:var(--ink);text-transform:capitalize}

/* why */
.why-band{left:0;top:1642px;width:1200px;height:970px;background:var(--ice)}
.why-photo{left:58px;top:1902px;width:527px;height:661px;border-radius:13px;background:linear-gradient(135deg,#f3f5f7 0%,#c9d6e6 45%,#4d6f9d 100%)}
.benefits{left:620px;top:1900px;width:520px;list-style:none}
.benefits li{position:relative;padding-left:45px;height:133px}
.benefits svg{position:absolute;left:0;top:4px}
.benefits h4{font-size:19px;font-weight:600;line-height:30px}
.benefits p{font-size:16px;line-height:25px;color:var(--text);text-transform:capitalize;margin-top:4px}

/* process */
.steps{left:28px;top:2840px;width:1144px;display:grid;grid-template-columns:repeat(4,1fr);text-align:center}
.step b{display:block;font-size:37px;font-weight:600;color:var(--blue);line-height:50px}
.step h3{font-size:23px;font-weight:600;margin:12px 0 14px}
.step p{font-size:16px;line-height:25px;color:var(--ink);text-transform:capitalize;padding:0 40px}

/* cta */
.cta-band{left:0;top:3170px;width:1200px;height:272px;background:var(--ice)}
.cta-title{font-size:30px;font-weight:600;color:var(--blue)}
.cta-copy{font-size:23px;line-height:37px;color:var(--text)}

/* footer */
.rule{left:60px;width:1080px;height:1px;background:#9ca3af}
.footer-mark{left:133px;top:3550px;display:flex;align-items:center;gap:10px;font-size:17px;font-weight:600;color:var(--ink)}
.footer-copy{left:133px;top:3630px;width:440px;font-size:21px;line-height:30px;color:var(--blue)}
.foot-col h5{font-size:18px;font-weight:600;color:var(--blue);margin-bottom:18px}
.foot-col a{display:block;font-size:14px;color:var(--blue);text-decoration:none;margin-bottom:13px}
.copyright{font-size:11px;color:var(--navy)}
.socials{left:1000px;top:3783px;display:flex;gap:11px}
.socials span{width:30px;height:30px;border:2px solid var(--navy);border-radius:6px}
</style>
</head>
<body>

<!-- navigation -->
<div class="abs brand"><span class="brand-mark"></span>Crestline</div>
<nav class="abs nav-links">
  <span class="active">Home</span><span>Services</span><span>Benefits</span><span>Process</span><span>Contact</span>
</nav>
<svg class="abs theme-toggle" width="20" height="20" viewBox="0 0 24 24" fill="none" stroke="#374151" stroke-width="2"><path d="M21 12.8A9 9 0 1 1 11.2 3a7 7 0 0 0 9.8 9.8z"/></svg>
<a class="btn btn-solid" style="left:1022px;top:27px;width:113px;height:37px;font-size:14px">Kontakt</a>

<!-- hero -->
<div class="abs eyebrow" style="left:60px;top:112px">SQF Only · Tech Driven</div>
<h1 class="abs hero-title">Hire a tech-driven SQF team that carries you across the certification finish line</h1>
<p class="abs hero-copy">At Crestline Consulting Group, we focus exclusively on SQF — combining real plant experience with smart technology so your team can stay focused on production while we handle certification.</p>
<a class="btn btn-solid" style="left:60px;top:508px;width:204px;height:54px">Get SQF Consultation</a>
<a class="btn btn-ghost" style="left:281px;top:508px;width:165px;height:54px">Explore Services</a>
<div class="abs hero-photo" role="img" aria-label="Food production plant with lab technicians in protective wear inspecting samples beside stainless steel equipment"></div>

<div class="abs stats">
  <div class="stat"><b>15+</b><span>Clients Onboarded</span></div>
  <div class="stat"><b>100%</b><span>SQF Focused</span></div>
  <div class="stat"><b>90%</b><span>Digital Platform Built Programs</span></div>
  <div class="stat"><b>99%</b><span>US Nationwide Coverage</span></div>
</div>

<!-- services -->
<h2 class="abs center section-title" style="top:755px">SQF Consulting, Implementation &amp;<br>Onboarding</h2>
<p class="abs center section-sub" style="top:855px">We help food and beverage manufacturers achieve and maintain SQF certification with confidence, using<br>practical programs and digital tools that work on the floor — not just on audit day.</p>

<div class="abs cards">
  <div class="card">
    <div class="card-icon"><svg width="26" height="26" viewBox="0 0 24 24" fill="none" stroke="#0677BA" stroke-width="1.6"><rect x="3" y="4" width="18" height="16" rx="2"/><path d="M3 9h18M8 13h3M13 13h3M8 16h8"/></svg></div>
    <h3>SQF Program Design</h3>
    <p>We design your complete SQF system from scratch — HACCP/food safety plans, prerequisite programs, SOPs, forms, logs, and all required documentation tailored to your facility.</p>
  </div>
  <div class="card">
    <div class="card-icon"><svg width="26" height="26" viewBox="0 0 24 24" fill="none" stroke="#0677BA" stroke-width="1.6"><rect x="3" y="4" width="18" height="12" rx="1.5"/><path d="M9 20h6M12 16v4"/></svg></div>
    <h3>Digital Platform Build</h3>
    <p>We build your SQF program directly into modern food safety software like SafeBatch.io or PlantLedger.io — digitizing forms, checklists, monitoring logs, and workflows so your team runs paperless.</p>
  </div>
  <div class="card">
    <div class="card-icon"><svg width="26" height="26" viewBox="0 0 24 24" fill="none" stroke="#0677BA" stroke-width="1.6"><circle cx="12" cy="8" r="4"/><path d="M4 21c1-4 4-6 8-6s7 2 8 6"/></svg></div>
    <h3>Coaching &amp; Support</h3>
    <p>After building your system, we coach your team to own and maintain it day-to-day. You run the program; we provide ongoing expert guidance so you stay audit-ready at all times.</p>
  </div>
  <div class="card">
    <div class="card-icon"><svg width="26" height="26" viewBox="0 0 24 24" fill="none" stroke="#0677BA" stroke-width="1.6"><rect x="4" y="3" width="16" height="18" rx="2"/><circle cx="11" cy="11" r="3.5"/><path d="M13.5 13.5L17 17"/></svg></div>
    <h3>Gap Assessments</h3>
    <p>We evaluate where your facility stands against SQF requirements, identify gaps, and provide a clear roadmap to close them before your audit — no surprises on certification day.</p>
  </div>
  <div class="card">
    <div class="card-icon"><svg width="26" height="26" viewBox="0 0 24 24" fill="none" stroke="#0677BA" stroke-width="1.6"><circle cx="12" cy="7" r="3"/><circle cx="5" cy="10" r="2.2"/><circle cx="19" cy="10" r="2.2"/><path d="M6 20c0-3 3-6 6-6s6 3 6 6M1.5 18c.5-2 2-3 3.5-3M22.5 18c-.5-2-2-3-3.5-3"/></svg></div>
    <h3>Bilingual Team Support</h3>
    <p>Our team in Central America supports Spanish-speaking employees within your operation — delivering training, documentation, and coaching in the language your floor team actually speaks.</p>
  </div>
  <div class="card">
    <div class="card-icon"><svg width="26" height="26" viewBox="0 0 24 24" fill="none" stroke="#0677BA" stroke-width="1.6"><path d="M12 3l7 3v6c0 4.5-3 7.5-7 9-4-1.5-7-4.5-7-9V6z"/></svg></div>
    <h3>Sanitation &amp; Regulatory</h3>
    <p>From sanitation program design to environmental monitoring, we help you build internal capabilities that meet USDA, FDA, and FSMA requirements and reduce dependence on external contractors.</p>
  </div>
</div>

<!-- why -->
<div class="abs why-band"></div>
<div class="abs center eyebrow" style="top:1678px">Why Crestline</div>
<h2 class="abs center section-title" style="top:1703px">Built for Small &amp; Mid-Size<br>Manufacturers</h2>
<p class="abs center section-sub" style="top:1808px">You don't need to hire a full-time food safety director or figure out SQF alone. We<br>bring the expertise and technology — you stay focused on production</p>
<div class="abs why-photo" role="img" aria-label="Quality manager holding a tablet showing a food safety compliance checklist in a production facility"></div>
<ul class="abs benefits">
  <li><svg width="30" height="30" viewBox="0 0 24 24" fill="none" stroke="#0677BA" stroke-width="2"><path d="M20 8.5A9 9 0 1 1 16 4"/><path d="M8 11.5l3.5 3.5L21 5"/></svg><h4>Lower Cost Than A Full-Time Hire</h4><p>Get a complete SQF team — program design, digital implementation, and coaching — at a fraction of the cost of hiring a full-time SQF practitioner.</p></li>
  <li><svg width="30" height="30" viewBox="0 0 24 24" fill="none" stroke="#0677BA" stroke-width="2"><path d="M20 8.5A9 9 0 1 1 16 4"/><path d="M8 11.5l3.5 3.5L21 5"/></svg><h4>Your Program Lives In Software</h4><p>No more binders and spreadsheets. Your SQF system is built into SafeBatch.io or PlantLedger.io — organized, accessible, and always audit-ready.</p></li>
  <li><svg width="30" height="30" viewBox="0 0 24 24" fill="none" stroke="#0677BA" stroke-width="2"><path d="M20 8.5A9 9 0 1 1 16 4"/><path d="M8 11.5l3.5 3.5L21 5"/></svg><h4>You Own It, We Support It</h4><p>We build the system and train your team. You maintain and run it day-to-day. We stay on call with coaching and advisory so you never feel stuck.</p></li>
  <li><svg width="30" height="30" viewBox="0 0 24 24" fill="none" stroke="#0677BA" stroke-width="2"><path d="M20 8.5A9 9 0 1 1 16 4"/><path d="M8 11.5l3.5 3.5L21 5"/></svg><h4>Flexible, Low-Risk Engagement</h4><p>Start with a 3-month commitment, then go month-to-month. Cancel anytime with 30 days notice. We earn your business every month.</p></li>
  <li><svg width="30" height="30" viewBox="0 0 24 24" fill="none" stroke="#0677BA" stroke-width="2"><path d="M20 8.5A9 9 0 1 1 16 4"/><path d="M8 11.5l3.5 3.5L21 5"/></svg><h4>Bilingual Floor-Level Support</h4><p>With our Central America team, we provide training and documentation in Spanish so every member of your production team understands and follows the program.</p></li>
</ul>

<!-- process -->
<div class="abs center eyebrow" style="top:2690px">How It Works</div>
<h2 class="abs center section-title" style="top:2718px">From Discovery to Certification</h2>
<p class="abs center section-sub" style="top:2775px">A clear, structured path that takes the guesswork out of SQF.</p>
<div class="abs steps">
  <div class="step"><b>01</b><h3>Discovery Call</h3><p>We learn about your facility, your current systems, and where you are in the SQF journey. No pressure — just a conversation.</p></div>
  <div class="step"><b>02</b><h3>Gap Assessment</h3><p>We evaluate your facility against SQF requirements, identify what's missing, and give you a clear roadmap with priorities.<br>Build &amp; Implement</p></div>
  <div class="step"><b>03</b><h3>Build &amp; Implement</h3><p>We learn about your facility, your current systems, and where you are in the SQF journey. No pressure — just a conversation.</p></div>
  <div class="step"><b>04</b><h3>Coach &amp; Certify</h3><p>We learn about your facility, your current systems, and where you are in the SQF journey. No pressure — just a conversation.</p></div>
</div>

<!-- call to action -->
<div class="abs cta-band"></div>
<h2 class="abs center cta-title" style="top:3198px">Ready to Talk SQF?</h2>
<p class="abs center cta-copy" style="top:3255px">Share a few details about your facility and where you are in the SQF journey.<br>We'll follow up with a brief discovery call and a clear next step</p>
<a class="btn btn-solid" style="left:390px;top:3362px;width:205px;height:52px">Get SQF Consultation</a>
<a class="btn btn-ghost" style="left:617px;top:3362px;width:190px;height:52px">Visit Crestline</a>

<!-- footer -->
<div class="abs rule" style="top:3522px"></div>
<div class="abs footer-mark"><span class="brand-mark"></span>Crestline</div>
<p class="abs footer-copy">Tech-driven SQF consulting for small and mid-size US food manufacturers. Based in Fresno, CA — serving clients across North America.</p>
<div class="abs foot-col" style="left:690px;top:3548px">
  <h5>Navigate</h5><a>Services</a><a>Benefits</a><a>Process</a><a>Contact</a>
</div>
<div class="abs foot-col" style="left:875px;top:3548px">
  <h5>Connect</h5><a>info@crestlineconsulting.io</a><a style="text-decoration:underline">CrestlineConsulting.io</a>
</div>
<div class="abs rule" style="top:3765px"></div>
<p class="abs center copyright" style="top:3790px">© 2026 Crestline Consultant. All rights reserved.</p>
<div class="abs socials"><span></span><span></span><span></span></div>

</body>
</html>
```